Need a cover for eBook:
Title is: 47 Blunders That Sink Your Indie-Released eBook.
Remarks about the title: I know that is difficult to design a cover with a number. You can add the word TOP (in caps or not) before 47 blunders. It is not mandatory to insert the word TOP. It is up to you if you think you can create a better cover.
Subtitle is: A Newcomer's Manual for Releasing Solo, Shaping Pictures and Words, Arranging Pages, Boosting Sign-ups and Moving More Copies
Author: Dennis R. Albrook
Publisher: Lanternfield Works
The book made the presentation of errors that can occur during the production of an ebook. Title must be big, the title should be readable even when the image is reduced in size. No photo please.
I join my projects as an example. Do what you want but I need impact.

Target Market(s)

Book to sell first at Brisco Leafreader Shop. Target is authors, men or women, who want to produce ebooks.

Industry/Entity Type

Publishing Company

Font styles to use
Sans Serif

Colors
3176b5
9bcb3c

Requirements
Must have
• High readability when cover is small.
• Here is the definition of the word KILL
• put an end to or cause the failure or defeat of (something).
• "the committee voted to kill the project"
• synonyms: destroy, put an end to, end, extinguish, dash, quash, ruin, wreck, shatter, smash, crush, scotch, thwart; informalput the kibosh on, stymie, scuttle
• "this would kill all hopes of progress"
• veto, defeat, vote down, rule against, reject, throw out, overrule, overturn, put a stop to, quash, squash
• "an opposition attempt to kill the bill"
Nice to have
• I suggested 2 colors but you can you use another one or two. I want cover that sell. There is so bright ideas here. Come on down!
Should not have
• No picture or photo. If a photo or an object had power to the cover, you can insert one. I don't want a photo-collage.

```html
<!DOCTYPE html>
<html lang="en">
<head>
<meta charset="utf-8">
<title>47 Blunders That Sink Your Indie-Released eBook — Dennis R. Albrook</title>
<link rel="stylesheet" href="https://fonts.googleapis.com/css2?family=Montserrat:wght@600;700;800&display=swap">
<style>
  :root {
    --cover-blue: #3a7ec0;
    --cover-blue-deep: #2f6fae;
    --paper-grey: #d9d9d9;
    --tear-green: #9bcb3c;
    --ink-dark: #4a4a4a;
    --ink-light: #d6d6d6;
    --publisher-green: #8cc63f;
  }
  html, body {
    margin: 0;
    padding: 0;
    width: 800px;
    height: 1200px;
    overflow: hidden;
    background: var(--cover-blue);
  }
  .book-cover {
    display: block;
    width: 800px;
    height: 1200px;
  }
  .cover-background { fill: var(--cover-blue); }
  .tear-edge { fill: var(--tear-green); }
  .paper-band { fill: var(--paper-grey); }
  .author-name,
  .title-number,
  .title-keyword,
  .title-rest,
  .subtitle,
  .publisher-name {
    font-family: "Montserrat", sans-serif;
    text-anchor: middle;
  }
  .author-name {
    font-size: 60px;
    font-weight: 800;
    fill: var(--ink-dark);
    letter-spacing: 2px;
  }
  .title-number {
    font-size: 176px;
    font-weight: 700;
    fill: var(--ink-light);
  }
  .title-keyword {
    font-size: 140px;
    font-weight: 800;
    fill: var(--ink-dark);
  }
  .title-rest {
    font-size: 116px;
    font-weight: 700;
    fill: var(--ink-light);
  }
  .title-rest .small-e { font-size: 86px; }
  .subtitle {
    font-size: 24px;
    font-weight: 800;
    fill: var(--ink-dark);
  }
  .publisher-name {
    font-size: 24px;
    font-weight: 800;
    fill: var(--publisher-green);
  }
</style>
</head>
<body>
<svg class="book-cover" viewBox="0 0 800 1200" xmlns="http://www.w3.org/2000/svg" role="img" aria-label="Book cover: 47 Blunders That Sink Your Indie-Released eBook by Dennis R. Albrook">
  <rect class="cover-background" x="0" y="0" width="800" height="1200"/>

  <text class="author-name" x="400" y="78" textLength="736" lengthAdjust="spacingAndGlyphs">DENNIS R. ALBROOK</text>

  <text class="title-number" x="400" y="252">47</text>

  <!-- middle torn paper band -->
  <path class="tear-edge" d="M0 272 L40 276 L70 270 L110 282 L150 278 L190 290 L230 286 L260 298 L300 300 L340 302 L380 300 L420 302 L470 298 L520 296 L560 284 L600 280 L640 276 L690 278 L740 274 L800 270 L800 330 L0 330 Z"/>
  <path class="tear-edge" d="M0 470 L800 470 L800 468 L760 472 L720 480 L680 478 L640 486 L600 484 L560 494 L520 492 L480 496 L440 494 L420 488 L380 490 L340 484 L300 486 L260 480 L0 478 Z"/>
  <path class="paper-band" d="M0 290 L30 294 L60 286 L90 300 L120 296 L150 306 L180 300 L210 310 L250 306 L290 314 L330 310 L370 316 L410 312 L450 316 L490 310 L530 314 L570 302 L610 306 L650 294 L690 300 L730 290 L770 296 L800 288 L800 462 L770 470 L740 466 L700 476 L660 470 L620 478 L580 474 L540 482 L500 478 L470 484 L430 476 L400 480 L360 470 L320 476 L280 466 L240 472 L200 464 L160 470 L120 462 L80 468 L40 460 L0 466 Z"/>

  <text class="title-keyword" x="400" y="444" textLength="734" lengthAdjust="spacingAndGlyphs">BLUNDERS</text>

  <text class="title-rest" x="400" y="606" textLength="640" lengthAdjust="spacingAndGlyphs">THAT SINK</text>
  <text class="title-rest" x="400" y="708" textLength="730" lengthAdjust="spacingAndGlyphs">YOUR INDIE-</text>
  <text class="title-rest" x="400" y="816" textLength="680" lengthAdjust="spacingAndGlyphs">RELEASED</text>
  <text class="title-rest" x="400" y="918"><tspan class="small-e">E</tspan>BOOK</text>

  <!-- bottom torn paper band -->
  <path class="tear-edge" d="M0 980 L40 972 L80 976 L120 966 L160 970 L200 958 L240 962 L280 950 L320 956 L360 946 L400 952 L440 944 L480 950 L520 940 L560 946 L600 936 L640 942 L680 934 L720 940 L760 932 L800 936 L800 1000 L0 1000 Z"/>
  <path class="paper-band" d="M0 996 L30 990 L70 994 L110 984 L150 988 L190 976 L230 982 L270 970 L310 976 L350 966 L390 972 L430 962 L470 968 L510 958 L550 964 L590 954 L630 960 L670 950 L710 956 L750 948 L800 954 L800 1200 L0 1200 Z"/>

  <text class="subtitle" x="400" y="1064" textLength="760" lengthAdjust="spacingAndGlyphs">A NEWCOMER'S MANUAL FOR RELEASING SOLO, SHAPING</text>
  <text class="subtitle" x="400" y="1094" textLength="760" lengthAdjust="spacingAndGlyphs">PICTURES AND WORDS, ARRANGING PAGES, BOOSTING</text>
  <text class="subtitle" x="400" y="1124">SIGN-UPS AND MOVING MORE COPIES</text>

  <text class="publisher-name" x="400" y="1166">LANTERNFIELD WORKS</text>
</svg>
</body>
</html>
```